Web Design Project

I need a three page website. I have designed the index.html and the specialevent.html page.

I need someone to finetune the pages for me.

Where I have difficulty is with the following:
I want to add an event table driven by php database.
The administrator of the event will login and create the wording that fits under each colmn. The administrator the submit the form to php database. The database then display in a html.

The Table contains 5 coloums and the rows can vary and can go up to as many as 100.

The table set out events on a program
In the last column of every row I need a submit button to "View and Book" I need to link those buttons with external links/pages.

I use Dreamweaver CS5 and I need to have it in this format in order for me to edit it in the future.

The Table needs to be updated once a year for this program. So ideally if someone has a password to update the certain regions this is what I have in mind.

I have also designed a mockup of the restaurant page. At the top I need.
1) 4 Colapsable panels
a) Restaurants - opening the names of the restaurants
b) Coffee shops and light lunches .... with the names
c) Family
d) Home eateries

From the colapsable panel of each of these I need a anchored link to the description/photos of each...with a BOOK now button I can submit bookings to.

I added a colapsable panel in each restaurants description to keep everything contained.

Please help

• Background must be fixed so that main.div scroll over it

The colours are chosen so please stick to it.

The green for the submit button I short is. #C8D707

I need to edit the pages in Dreamweaver CS5. /Flexilayout2pro

Please ask if you need to know anything. I exactly know what I want.

Kind regards
Marius Dreyer

The colours are fine.

The wording " havenridgeonline BOOKING agent" should appear right at the top in the white horizon part of the background image.

The specialevent page I described already. I am interested in the editable solution. for this.

I will make up a mockup of the third page and send it later.

Regards

```html
<!DOCTYPE html>
<html lang="en">
<head>
<meta charset="utf-8">
<title>Havenridge Online Booking Agent</title>
<link href="https://fonts.googleapis.com/css2?family=Oswald:wght@400;500;600&family=PT+Sans:ital,wght@0,400;0,700;1,400&display=swap" rel="stylesheet">
<style>
:root{
  --lime:#c8d707;
  --olive:#7a870a;
  --ink:#1b1b1b;
  --panel:#2c2c2c;
  --orange:#f26522;
  --grey-text:#555;
}
*{box-sizing:border-box;margin:0;padding:0}
html,body{width:929px;height:1200px;overflow:hidden}
body{position:relative;background:var(--ink);font-family:"PT Sans",sans-serif;color:#fff}
.hero-photo{position:absolute;left:0;top:0;width:929px;height:560px;
  background:linear-gradient(180deg,#ffffff 0,#f4f4f2 50px,#b9b8b2 90px,#8d8c85 180px,#6e6d66 300px,#4d4c47 400px,#2e2e2b 500px,var(--ink) 560px)}
.site-title{position:absolute;top:12px;left:0;width:929px;text-align:center;font-family:"Oswald",sans-serif;font-weight:600;font-size:31px;letter-spacing:-.5px;color:var(--ink);text-transform:uppercase}
.main-nav{position:absolute;left:93px;top:64px;width:743px;height:31px;border-radius:16px;background:linear-gradient(#c8d707,#a6b506);border:2px solid #d9e53a;box-shadow:0 2px 4px rgba(0,0,0,.4);display:flex;align-items:center}
.main-nav a{font-family:"Oswald",sans-serif;font-size:11px;color:#fff;text-decoration:none;text-transform:uppercase;margin-right:34px}
.main-nav a.active{background:#2a2a2a;height:31px;margin-top:-2px;margin-left:-2px;padding:0 17px 0 19px;line-height:31px;border-radius:16px 0 0 16px;margin-right:15px}
.search{position:absolute;right:6px;top:3px;width:158px;height:21px;border-radius:11px;background:#fff;border:1px solid #999}
.search svg{position:absolute;right:8px;top:5px}
.booking{position:absolute;left:93px;top:444px;width:743px;height:263px;background:var(--panel);border-radius:6px}
.booking h2{position:absolute;left:8px;top:12px;font-family:"Oswald",sans-serif;font-weight:400;font-style:italic;font-size:15px;color:var(--lime)}
.card{position:absolute;top:45px;width:232px;height:209px;background:#fff;border-radius:5px}
.card .btn{position:absolute;left:6px;top:7px;width:218px;height:100px;border-radius:6px;display:flex;align-items:center;justify-content:center;font-family:"Oswald",sans-serif;font-weight:500;font-size:29px;color:#fff;box-shadow:0 2px 3px rgba(0,0,0,.3)}
.stay{background:linear-gradient(#ff8a3d,#f04e1a)}
.play{background:linear-gradient(#b8c80e,#8fa005)}
.eat{background:linear-gradient(#23a8df,#0f6fb8)}
.card p{position:absolute;left:9px;top:124px;width:214px;text-align:center;font-size:12.4px;line-height:18.5px;color:var(--grey-text)}
.events{position:absolute;left:93px;top:723px;width:743px;height:203px;background:#fff;border-radius:6px;color:#333}
.events h2{position:absolute;left:8px;top:11px;font-family:"Oswald",sans-serif;font-weight:500;font-size:14px;color:var(--orange)}
.events .rule{position:absolute;left:8px;right:8px;height:1px;background:#ddd}
.event{position:absolute;left:8px;width:727px}
.event .date{position:absolute;left:0;top:0;width:54px;height:45px;background:#2e2e2e;border-radius:5px;text-align:center;font-family:"Oswald",sans-serif;line-height:1.2;padding-top:5px}
.event .date .d{color:var(--lime);font-size:13px;display:block}
.event .date .m{color:#fff;font-size:11.5px}
.event h3{position:absolute;left:62px;top:-1px;font-weight:400;font-size:12.5px;color:#9bad05}
.event p{position:absolute;left:62px;top:18px;width:665px;font-size:9px;line-height:14px;color:#333}
.contact{position:absolute;left:93px;top:938px;font-family:"Oswald",sans-serif}
.contact h2,.follow h2{font-weight:500;font-size:16px;color:var(--lime)}
.contact .lines{position:absolute;top:34px;width:220px;font-size:10px;line-height:13px;color:#bbb;text-transform:uppercase}
.contact .addr{left:191px}
.follow{position:absolute;left:724px;top:938px;font-family:"Oswald",sans-serif}
.social{display:flex;gap:5px;margin-top:8px}
.social span{width:24px;height:24px;background:#3a3a3a;border-radius:2px}
.footer{position:absolute;left:93px;top:1022px;width:743px;height:155px;border-radius:6px;background:linear-gradient(#c8d707,#a9b805);overflow:hidden;color:#222}
.footer .copy{height:32px;background:var(--olive);color:#fff;font-size:10px;line-height:32px;padding-left:8px}
.footer h3{position:absolute;font-family:"Oswald",sans-serif;font-weight:500;font-size:12px;color:#111}
.services{position:absolute;left:8px;top:44px;width:287px}
.services h3{position:static;margin-bottom:6px}
.services a{display:block;border-top:1px solid #7e8b06;font-size:10px;color:#222;text-decoration:none;padding:8px 0 7px}
.newsletter h3{left:487px;top:44px}
.newsletter .field{position:absolute;left:487px;top:71px;width:236px;height:28px;background:#fff;border-radius:14px;border:2px solid #e9ef9e}
.newsletter .submit{position:absolute;left:649px;top:111px;width:73px;height:28px;border-radius:14px;background:#1e1e1e;color:#e9ef9e;font-family:"Oswald",sans-serif;font-size:12px;text-align:center;line-height:28px}
</style>
</head>
<body>
<div class="hero-photo" role="img" aria-label="Black and white landscape of a small Karoo town with a church steeple, trees and mountains behind"></div>

<h1 class="site-title">Havenridge Online Booking Agent</h1>

<nav class="main-nav">
  <a class="active" href="#">Home</a>
  <a href="#">Accommodation</a>
  <a href="#">Play</a>
  <a href="#">Contact</a>
  <div class="search"><svg width="9" height="9" viewBox="0 0 9 9"><circle cx="3.5" cy="3.5" r="2.5" fill="none" stroke="#555" stroke-width="1.2"/><line x1="5.3" y1="5.3" x2="8.3" y2="8.3" stroke="#555" stroke-width="1.4"/></svg></div>
</nav>

<section class="booking">
  <h2>Your booking agent for</h2>
  <div class="card" style="left:8px">
    <div class="btn stay">Lodging</div>
    <p>Find the perfect accommodation to suit your specific needs. Click on Lodging to view and book our properties online Now!</p>
  </div>
  <div class="card" style="left:255px">
    <div class="btn play">Outings</div>
    <p>Secure your Playlist! Havenridge has wonderful excurions, activities, shows and festival on offer. Click on Outings and book it all ONLINE!</p>
  </div>
  <div class="card" style="left:503px">
    <div class="btn eat">Dining</div>
    <p>Wow! Book your eating experience with us. As always Havenridge has the best on offer to enhance your cullinary experience. Click Dining !</p>
  </div>
</section>

<section class="events">
  <h2>SPECIAL EVENTS AND FESTIVALS</h2>
  <div class="rule" style="top:38px"></div>
  <div class="event" style="top:56px">
    <div class="date"><span class="d">01</span><span class="m">August</span></div>
    <h3>Olive Festival - April 2014</h3>
    <p>Lorem ipsum dolor sit amet, consectetur adipisicing elit, sed do eiusmod tempor incididunt ut labore et dolore magna aliqua. Ut enim ad minim veniam, quis nostrud exercitation ullamco laboris nisi ut aliquip ex ea commodo consequat. Duis aute irure dolor in reprehenderit in voluptate velit esse</p>
  </div>
  <div class="rule" style="top:124px"></div>
  <div class="event" style="top:142px">
    <div class="date"><span class="d">01</span><span class="m">August</span></div>
    <h3>Olive Festival - April 2014</h3>
    <p>Lorem ipsum dolor sit amet, consectetur adipisicing elit, sed do eiusmod tempor incididunt ut labore et dolore magna aliqua. Ut enim ad minim veniam, quis nostrud exercitation ullamco laboris nisi ut aliquip ex ea commodo consequat. Duis aute irure dolor in reprehenderit in voluptate velit esse</p>
  </div>
</section>

<section class="contact">
  <h2>CONTACT US</h2>
  <div class="lines">Phone: 0861 302118<br>E-mail: admin@hronline.biz</div>
  <div class="lines addr">Address:<br>&nbsp;Mill Lane, Havenridge</div>
</section>

<section class="follow">
  <h2>FOLLOW US</h2>
  <div class="social" aria-label="Social links"><span></span><span></span><span></span><span></span></div>
</section>

<footer class="footer">
  <div class="copy">©2013 hronline. All Rights Reserved. Privacy Policy.</div>
  <div class="services">
    <h3>SERVICES</h3>
    <a href="#">Business Directory</a>
    <a href="#">Relevant Links &amp; Websites</a>
    <a href="#">Emergency Numbers</a>
  </div>
  <div class="newsletter">
    <h3>NEWSLETTR SIGNUP</h3>
    <div class="field"></div>
    <div class="submit">SIGHUP</div>
  </div>
</footer>
</body>
</html>
```